Criação de Kit Layout de Posts para Redes Sociais (Facebook, Instagram e etc) para Roupas, Jóias & acessórios
" Funcionará por internet site e Instagram "

```html
<!DOCTYPE html>
<html lang="pt-BR">
<head>
<meta charset="UTF-8">
<title>Bolsas e Utilitários — Bella Marchand</title>
<link href="https://fonts.googleapis.com/css2?family=Montserrat:wght@500;600;800&display=swap" rel="stylesheet">
<style>
  :root {
    --teal: #3bbcc8;
    --black: #111111;
    --white: #ffffff;
    --denim-dark: #2d3b58;
    --denim: #55698e;
    --leather: #d9a27c;
    --leather-light: #ecc6a6;
    --backdrop: #9aa38a;
  }
  * { margin: 0; padding: 0; box-sizing: border-box; }
  html, body { width: 1200px; height: 1200px; overflow: hidden; background: var(--white); }
  .post {
    position: relative;
    width: 1200px;
    height: 1200px;
    overflow: hidden;
    font-family: 'Montserrat', Arial, sans-serif;
  }
  .photo {
    position: absolute;
    inset: 0;
    background:
      radial-gradient(ellipse 45% 55% at 75% 50%, var(--leather-light) 0%, var(--leather) 45%, rgba(217,162,124,0) 75%),
      linear-gradient(100deg, var(--denim-dark) 0%, var(--denim) 30%, var(--denim-dark) 52%, var(--backdrop) 100%);
  }
  .shapes { position: absolute; inset: 0; }
  .headline {
    position: absolute;
    left: 62px;
    top: 70px;
    padding-left: 46px;
    border-left: 12px solid var(--teal);
    color: var(--white);
  }
  .headline__title {
    font-weight: 800;
    font-size: 88px;
    line-height: 0.98;
    letter-spacing: 1px;
    text-transform: uppercase;
  }
  .headline__categories {
    margin-top: 26px;
    font-weight: 600;
    font-size: 31px;
    line-height: 1.2;
    letter-spacing: 1.5px;
    text-transform: uppercase;
  }
  .brand {
    position: absolute;
    right: 62px;
    bottom: 40px;
    width: 400px;
    text-align: center;
    color: var(--white);
  }
  .brand__mark {
    width: 96px;
    height: 96px;
    margin: 0 auto 22px;
    border-radius: 50%;
    background: var(--white);
  }
  .brand__name {
    font-weight: 500;
    font-size: 40px;
    letter-spacing: 1px;
    text-transform: uppercase;
  }
  .brand__tagline {
    margin-top: 6px;
    font-weight: 500;
    font-size: 17px;
    letter-spacing: 7px;
    text-transform: uppercase;
  }
</style>
</head>
<body>
  <main class="post">
    <div class="photo" role="img" aria-label="Fotografia de uma pessoa com camisa listrada azul e relógio segurando uma bolsa saco de couro caramelo com alças amarradas"></div>

    <svg class="shapes" viewBox="0 0 1200 1200" width="1200" height="1200" aria-hidden="true">
      <polygon points="0,900 0,1200 450,1200" fill="var(--black)"/>
      <polygon points="1200,763 1200,1200 336,1200" fill="var(--teal)"/>
    </svg>

    <header class="headline">
      <h1 class="headline__title">Bolsas e<br>Utilitários</h1>
      <p class="headline__categories">Casual - Social<br>Moda Praia - Academia</p>
    </header>

    <footer class="brand">
      <div class="brand__mark"></div>
      <p class="brand__name">Bella Marchand</p>
      <p class="brand__tagline">Bolsas e Utilitários</p>
    </footer>
  </main>
</body>
</html>
```